New Business Cards for Torvin Group

We need a new Business Card to compliment our new logo. We are a vibrant design, manufacture and install business providing recreation areas, public parks and Municipal spaces. We want business cards that are classy, modern and clean.

We have recently changed our logo, and are celebrating our 40th anniversary. We want business cards with a new modern design to reflect our status.

Target Market(s)

Customers

Contact Information for Business Card

We need all the details of our 3 offices as per the business card attached. Please disregard the old logo on the business card, the other three files show our new logo.

Requirements
Must have
• All info as per attached business card but with new logo.
Nice to have

```html
<!DOCTYPE html>
<html lang="en">
<head>
<meta charset="utf-8">
<title>Torvin Group – Business Card</title>
<link rel="stylesheet" href="https://fonts.googleapis.com/css2?family=Lato:wght@400;700&display=swap">
<style>
  :root {
    --backdrop: #3b3b3b;
    --card: #f4f4f4;
    --red: #d9434d;
    --red-deep: #c93a44;
    --ink: #3c3c3c;
    --ink-soft: #4a4a4a;
    --ghost: rgba(0,0,0,0.045);
    --ghost-red: rgba(217,67,77,0.07);
  }
  * { margin: 0; padding: 0; box-sizing: border-box; }
  html, body {
    width: 1033px; height: 1200px; overflow: hidden;
    background: var(--backdrop);
    font-family: "Lato", sans-serif;
  }
  .card {
    position: absolute; left: 36px; top: 326px;
    width: 960px; height: 548px;
    background: var(--card);
    overflow: hidden;
    color: var(--ink);
  }
  .card-decor { position: absolute; inset: 0; }
  .ghost-name {
    position: absolute; left: 60px; top: 170px;
    font-size: 210px; font-weight: 700; letter-spacing: 4px;
    color: var(--ghost); white-space: nowrap; line-height: 1;
  }
  .brand {
    position: absolute; left: 40px; top: 112px;
    display: flex; align-items: center; gap: 16px;
  }
  .brand-dot {
    width: 54px; height: 54px; border-radius: 50%;
    background: var(--red);
  }
  .brand-name {
    font-size: 44px; font-weight: 700; color: var(--ink-soft);
    white-space: nowrap;
  }
  .person {
    position: absolute; right: 72px; top: 38px; text-align: right; color: #fff;
  }
  .person-name { font-size: 48px; font-weight: 400; line-height: 56px; }
  .person-title { font-size: 27px; line-height: 32px; }
  .direct {
    position: absolute; right: 72px; top: 150px; text-align: right;
    font-size: 28px; line-height: 32px; color: var(--ink);
  }
  .offices {
    position: absolute; left: 38px; top: 328px; width: 900px;
  }
  .office { position: absolute; top: 0; white-space: nowrap; }
  .office:nth-child(1) { left: 0; }
  .office:nth-child(2) { left: 321px; }
  .office:nth-child(3) { left: 633px; }
  .office-title { font-size: 30px; font-weight: 400; line-height: 36px; color: var(--ink); }
  .office-line { font-size: 18px; line-height: 24.6px; color: var(--ink-soft); }
  .web-band {
    position: absolute; left: 0; top: 476px; width: 960px; height: 42px;
    background: linear-gradient(90deg, var(--red), var(--red-deep));
    color: #fff; text-align: center;
    font-size: 33px; line-height: 42px; letter-spacing: 5px;
    padding-right: 10px;
  }
</style>
</head>
<body>
  <div class="card">
    <svg class="card-decor" width="960" height="548" viewBox="0 0 960 548">
      <circle cx="150" cy="150" r="215" fill="none" stroke="var(--ghost-red)" stroke-width="34"/>
      <polygon points="522,30 960,30 960,141 481,141" fill="var(--red)"/>
    </svg>
    <div class="ghost-name" aria-hidden="true">TORVIN</div>

    <div class="brand">
      <span class="brand-dot"></span>
      <span class="brand-name">Torvin Group</span>
    </div>

    <div class="person">
      <p class="person-name">Daren Keswick</p>
      <p class="person-title">Managing Partner</p>
    </div>

    <div class="direct">
      <p>Mobile No: +971(0)50 384 7720</p>
      <p>Email: daren@torvingroup.com</p>
    </div>

    <div class="offices">
      <div class="office">
        <h2 class="office-title">Head Office</h2>
        <p class="office-line">P.O. Box: 41820 Abu Dhabi, U.A.E.</p>
        <p class="office-line">Tel No: +971(0)2 5531907</p>
        <p class="office-line">Fax No: +971(0)2 5531908</p>
        <p class="office-line">Email: sales@torvingroup.com</p>
      </div>
      <div class="office">
        <h2 class="office-title">Dubai Office</h2>
        <p class="office-line">P.O. Box: 275146 Dubai, U.A.E.</p>
        <p class="office-line">Tel No: +971(0)4 4683052</p>
        <p class="office-line">Fax No: +971(0)4 4683170</p>
        <p class="office-line">Email: sales@torvingroup.com</p>
      </div>
      <div class="office">
        <h2 class="office-title">Qatar Office</h2>
        <p class="office-line">P.O. Box: 20873 Doha, Qatar.</p>
        <p class="office-line">Tel No: +974 44517306</p>
        <p class="office-line">Fax No: +974 44731582</p>
        <p class="office-line">Email: sales@torvingroup.com</p>
      </div>
    </div>

    <div class="web-band">www.torvingroup.com</div>
  </div>
</body>
</html>
```